1 Page Bio, describing our Mission to buy multifamily properties in Colorado Springs.

I am uploading a sample of an associate who is doing a similar thing in Tampa Florida. I will also upload an attempt by my assistant to make the flyer and I will upload 3 pictures to use, along with another document that has text to add. I want to be able to edit the document pretty easily inside a google doc. thanks, I want it to look clean and professional.

```html
<!DOCTYPE html>
<html lang="en">
<head>
<meta charset="utf-8">
<title>Multifamily Investor Bio – Colorado Springs</title>
<link href="https://fonts.googleapis.com/css2?family=Open+Sans:wght@300;400;600;700;800&family=Oswald:wght@500;600&display=swap" rel="stylesheet">
<style>
  :root {
    --page-bg: #e6e6e4;
    --paper: #ffffff;
    --brand-blue: #3a7ca6;
    --brand-blue-light: #5d9bc2;
    --slate: #476882;
    --heading-blue: #2d6b95;
    --body-grey: #6a6f74;
    --icon-bg: #dfe8ef;
    --rule: #c9d3db;
  }
  * { box-sizing: border-box; margin: 0; padding: 0; }
  html, body { width: 1200px; height: 800px; overflow: hidden; }
  body {
    background: var(--page-bg);
    font-family: "Open Sans", Arial, sans-serif;
    position: relative;
  }
  .flyer {
    position: absolute; left: 298px; top: 10px;
    width: 604px; height: 780px;
    background: var(--paper);
    overflow: hidden;
    box-shadow: 0 2px 10px rgba(0,0,0,.12);
  }
  .abs { position: absolute; }

  /* Header */
  .hero-photo {
    left: 290px; top: 0; width: 314px; height: 197px;
    background: linear-gradient(180deg, #e9e2d6 0%, #d8cbb8 30%, #9c7f66 55%, #6e6a66 78%, #a7a69b 100%);
  }
  .hero-panel { left: 0; top: 0; }
  .logo-text {
    left: 24px; top: 22px;
    color: #fff; font-weight: 700; font-size: 40px; letter-spacing: .5px;
  }
  .mission-label {
    left: 24px; top: 84px; color: #fff; font-weight: 700; font-size: 13.5px;
  }
  .mission-text {
    left: 27px; top: 110px; width: 270px;
    color: #fff; font-weight: 400; font-size: 15px; line-height: 20.5px;
  }

  /* Why columns */
  .why-col { top: 212px; }
  .why-col.multifamily { left: 30px; }
  .why-col.location { left: 318px; }
  .why-icon { position: absolute; left: 0; top: 0; }
  .why-title {
    position: absolute; top: 10px; white-space: nowrap;
    color: var(--heading-blue); font-weight: 700; font-size: 15px;
  }
  .multifamily .why-title { left: 52px; }
  .location .why-title { left: 44px; }
  .why-list {
    position: absolute; top: 36px; list-style: none; white-space: nowrap;
    color: var(--body-grey); font-size: 11px; line-height: 15.5px;
  }
  .multifamily .why-list { left: 52px; }
  .location .why-list { left: 44px; }
  .why-list li::before { content: "• "; }
  .column-rule { left: 301px; top: 232px; width: 1px; height: 98px; background: var(--rule); }

  /* Strategy */
  .strategy-title {
    left: 0; top: 348px; width: 604px; text-align: center;
    color: var(--heading-blue); font-weight: 700; font-size: 15.5px;
  }
  .strategy-card {
    top: 397px; height: 147px; background: var(--slate); color: #fff;
  }
  .strategy-card.acquire { left: 24px; width: 181px; }
  .strategy-card.reposition { left: 212px; width: 181px; background: var(--brand-blue); }
  .strategy-card.refinance { left: 400px; width: 182px; }
  .card-icon {
    position: absolute; left: 50%; top: -23px; margin-left: -23px;
    width: 46px; height: 46px; border-radius: 50%; background: var(--icon-bg);
    display: flex; align-items: center; justify-content: center;
  }
  .card-title {
    position: absolute; top: 33px; width: 100%; text-align: center;
    font-size: 11.5px; font-weight: 400; letter-spacing: .2px;
  }
  .card-list {
    position: absolute; top: 55px; left: 13px; right: 8px; list-style: none;
    font-size: 8.6px; line-height: 10.8px;
  }
  .card-list li::before { content: "• "; }
  .refinance .card-list li { margin-bottom: 10.8px; }

  /* Team */
  .team-band { left: 0; top: 561px; width: 604px; height: 166px; background: var(--slate); color: #fff; }
  .team-title {
    position: absolute; top: 3px; width: 100%; text-align: center;
    font-weight: 700; font-size: 15px;
  }
  .team-photo { position: absolute; border-radius: 50%; border: 2px solid #fff; }
  .team-photo.principals {
    left: 18px; top: 39px; width: 104px; height: 104px;
    background: radial-gradient(circle at 50% 40%, #8a8d72 0%, #5f6a4e 50%, #3f4a3a 100%);
  }
  .team-photo.advisor-one {
    left: 328px; top: 18px; width: 58px; height: 58px;
    background: radial-gradient(circle at 50% 45%, #e2d0c4 0%, #c9c9c9 60%, #f2f2f2 100%);
  }
  .team-photo.advisor-two {
    left: 328px; top: 78px; width: 58px; height: 58px;
    background: radial-gradient(circle at 50% 45%, #d8b9a4 0%, #bdbdbd 60%, #efefef 100%);
  }
  .team-rule { position: absolute; left: 301px; top: 36px; width: 1px; height: 116px; background: rgba(255,255,255,.45); }
  .team-text {
    position: absolute; font-size: 6.3px; line-height: 8.1px;
  }
  .team-text.principals { left: 131px; top: 28px; width: 168px; }
  .team-text.advisors { left: 400px; top: 28px; width: 196px; }
  .team-heading { font-size: 8px; font-weight: 600; margin-bottom: 3px; }
  .member-name { font-size: 7px; font-weight: 600; }
  .member-list { list-style: none; margin-bottom: 3px; }
  .member-list li::before { content: "• "; }

  /* Footer */
  .footer-name {
    left: 27px; top: 744px; color: var(--heading-blue);
    font-family: "Oswald", "Arial Narrow", sans-serif; font-weight: 500; font-size: 18.5px;
    letter-spacing: -.2px;
  }
  .footer-rule { top: 737px; width: 1px; height: 34px; background: #9aa9b5; }
  .footer-rule.first { left: 212px; }
  .footer-rule.second { left: 398px; }
  .phone-icon { left: 224px; top: 737px; }
  .phone-number {
    left: 258px; top: 731px; color: var(--heading-blue);
    font-family: "Oswald", "Arial Narrow", sans-serif; font-weight: 600; font-size: 20px;
  }
  .email { left: 258px; top: 757px; color: var(--heading-blue); font-weight: 700; font-size: 11.5px; }
  .social { top: 743px; width: 22px; height: 22px; border-radius: 50%; background: var(--brand-blue); }
</style>
</head>
<body>
<main class="flyer">

  <!-- Header -->
  <div class="abs hero-photo" role="img" aria-label="Photo of a modern multifamily apartment building"></div>
  <svg class="abs hero-panel" width="350" height="197" viewBox="0 0 350 197" aria-hidden="true">
    <polygon points="0,0 304,0 348,98 304,197 0,197" fill="#5d9bc2"/>
    <polygon points="0,0 297,0 341,98 297,197 0,197" fill="#3a7ca6"/>
  </svg>
  <h1 class="abs logo-text">YOUR LOGO</h1>
  <h2 class="abs mission-label">THE MISSION:</h2>
  <p class="abs mission-text">To create a family business by purchasing Multifamily Residences, one at a time.</p>

  <!-- Why columns -->
  <section class="abs why-col multifamily">
    <svg class="why-icon" width="40" height="40" viewBox="0 0 40 40" aria-hidden="true">
      <g fill="#2d6b95">
        <rect x="3" y="4" width="18" height="34"/>
        <rect x="22" y="14" width="16" height="24"/>
      </g>
      <g fill="#fff">
        <rect x="6" y="8" width="4" height="4"/><rect x="14" y="8" width="4" height="4"/>
        <rect x="6" y="16" width="4" height="4"/><rect x="14" y="16" width="4" height="4"/>
        <rect x="6" y="24" width="4" height="4"/><rect x="14" y="24" width="4" height="4"/>
        <rect x="25" y="18" width="4" height="4"/><rect x="31" y="18" width="4" height="4"/>
        <rect x="25" y="26" width="4" height="4"/><rect x="31" y="26" width="4" height="4"/>
        <rect x="10" y="31" width="4" height="7"/>
      </g>
    </svg>
    <h3 class="why-title">WHY MULTIFAMILY?</h3>
    <ul class="why-list">
      <li>Earn Monthly Cashflow</li>
      <li>Huge Tax Benefits</li>
      <li>Passive Income</li>
      <li>Historically Stable Investments</li>
      <li>Economies of Scale</li>
      <li>Housing is an enduring need</li>
    </ul>
  </section>
  <div class="abs column-rule"></div>
  <section class="abs why-col location">
    <svg class="why-icon" width="34" height="38" viewBox="0 0 34 38" aria-hidden="true">
      <g fill="none" stroke="#2d6b95" stroke-width="2">
        <rect x="4" y="5" width="26" height="31" rx="2"/>
        <rect x="12" y="2" width="10" height="6" rx="1" fill="#fff"/>
        <polyline points="8,15 10,17 13,13"/><line x1="16" y1="15" x2="26" y2="15"/>
        <polyline points="8,22 10,24 13,20"/><line x1="16" y1="22" x2="26" y2="22"/>
        <polyline points="8,29 10,31 13,27"/><line x1="16" y1="29" x2="26" y2="29"/>
      </g>
    </svg>
    <h3 class="why-title">WHY COLORADO SPRINGS?</h3>
    <ul class="why-list">
      <li>Strong Job Growth 2.91%</li>
      <li>Robust Population Growth 1.95%</li>
      <li>20.5% Population increase by 2030</li>
      <li>Low Unemployment Rate 2.9%</li>
      <li>Many large firms relocating to Tampa</li>
    </ul>
  </section>

  <!-- Investment strategy -->
  <h2 class="abs strategy-title">INVESTMENT STRATEGY</h2>

  <section class="abs strategy-card acquire">
    <div class="card-icon">
      <svg width="24" height="24" viewBox="0 0 24 24" aria-hidden="true">
        <g fill="#3a7ca6"><rect x="2" y="8" width="9" height="15"/><rect x="12" y="3" width="10" height="20"/></g>
        <g fill="#dfe8ef"><rect x="4" y="11" width="2" height="2"/><rect x="7" y="11" width="2" height="2"/><rect x="4" y="16" width="2" height="2"/><rect x="7" y="16" width="2" height="2"/><rect x="14" y="6" width="2" height="2"/><rect x="18" y="6" width="2" height="2"/><rect x="14" y="11" width="2" height="2"/><rect x="18" y="11" width="2" height="2"/><rect x="14" y="16" width="2" height="2"/><rect x="18" y="16" width="2" height="2"/></g>
      </svg>
    </div>
    <h3 class="card-title">ACQUIRE:</h3>
    <ul class="card-list">
      <li>Purchase Underperforming</li>
      <li>Purchase Underperforming</li>
      <li>Apartment Communities</li>
      <li>Mom and Pop Characteristics</li>
      <li>Class B and C buildings</li>
      <li>20-50 units</li>
      <li>Deferred maintenance</li>
      <li>Value-Add opportunity</li>
    </ul>
  </section>

  <section class="abs strategy-card reposition">
    <div class="card-icon">
      <svg width="30" height="22" viewBox="0 0 30 22" aria-hidden="true">
        <g fill="#3a7ca6">
          <circle cx="6" cy="7" r="3"/><circle cx="24" cy="7" r="3"/><circle cx="15" cy="5" r="4"/>
          <path d="M1 18 a5 5 0 0 1 10 0 z"/><path d="M19 18 a5 5 0 0 1 10 0 z"/>
          <path d="M8 20 a7 7 0 0 1 14 0 z"/>
        </g>
      </svg>
    </div>
    <h3 class="card-title">REPOSITION</h3>
    <ul class="card-list">
      <li>Hire professional management team</li>
      <li>Stabilize the property</li>
      <li>Fill vacancies</li>
      <li>Implement RUBS</li>
      <li>Change fee structure</li>
      <li>Raise remaining rents</li>
    </ul>
  </section>

  <section class="abs strategy-card refinance">
    <div class="card-icon">
      <svg width="24" height="22" viewBox="0 0 24 22" aria-hidden="true">
        <g fill="#3a7ca6">
          <rect x="3" y="14" width="3" height="7"/><rect x="8" y="11" width="3" height="10"/>
          <rect x="13" y="8" width="3" height="13"/><rect x="18" y="5" width="3" height="16"/>
        </g>
        <polyline points="2,11 8,6 12,8 20,1" fill="none" stroke="#3a7ca6" stroke-width="1.6"/>
        <polygon points="21,0 22,5 17,2" fill="#3a7ca6"/>
      </svg>
    </div>
    <h3 class="card-title">REFINANCE &amp; PROCEEDS:</h3>
    <ul class="card-list">
      <li>Refinance the property and roll proceeds into the next</li>
      <li>Sell the property and cash out or roll into the next property</li>
    </ul>
  </section>

  <!-- Team -->
  <section class="abs team-band">
    <h2 class="team-title">MEET THE TEAM</h2>
    <div class="team-photo principals" role="img" aria-label="Photo of the two principals standing outdoors"></div>
    <div class="team-text principals">
      <p class="team-heading">HARLOW TEAM / PRINCIPALS</p>
      <p class="member-name">Ryan Harlow</p>
      <ul class="member-list">
        <li>Licensed Colorado Real Estate Agent 18 years</li>
        <li>Broker-Owner of two Keystone Realty offices 7 and 2 Years</li>
        <li>Real Estate investing for 5 years</li>
        <li>Member of Summit Wealth Academy</li>
        <li>Married 24 years to Anne, parenting 10 children together</li>
        <li>Appeared on the Open Door Multifamily Show</li>
        <li>$2M portfolio</li>
      </ul>
      <p class="member-name">Craig Harlow</p>
      <ul class="member-list">
        <li>Retired Electrical Engineer</li>
        <li>Active Real Estate Investor/Consultant</li>
        <li>Net worth over $4M</li>
        <li>15 Grandchildren</li>
      </ul>
    </div>
    <div class="team-rule"></div>
    <div class="team-photo advisor-one" role="img" aria-label="Headshot of advisor Dean Archer"></div>
    <div class="team-photo advisor-two" role="img" aria-label="Headshot of advisor Ben Hollis"></div>
    <div class="team-text advisors">
      <p class="team-heading">ADVISORS</p>
      <p class="member-name">Dean Archer</p>
      <ul class="member-list">
        <li>General partner on 103 Apartments</li>
        <li>Acquiring 101 more apartments in Q1 - 2020</li>
        <li>Flips 4-8 houses a year</li>
        <li>Active member in the Apex Investor Community</li>
        <li>Accountability coach</li>
      </ul>
      <p class="member-name" style="margin-top:8px">Ben Hollis</p>
      <ul class="member-list">
        <li>He has been in the real estate business for 13 years and has created a portfolio of over 1000 units while growing Ridgeline Management with a team of 15 staff members.</li>
        <li>He has taught real estate for the past 6 years and has dozens of highly successful students. Ben uses his extensive real estate experience to teach his students the "real" side of real estate.</li>
      </ul>
    </div>
  </section>

  <!-- Footer -->
  <p class="abs footer-name">RYAN &amp; CRAIG HARLOW</p>
  <div class="abs footer-rule first"></div>
  <svg class="abs phone-icon" width="24" height="36" viewBox="0 0 24 36" aria-hidden="true">
    <rect x="2" y="1" width="20" height="34" rx="3" fill="none" stroke="#2d6b95" stroke-width="2.4"/>
    <line x1="2" y1="27" x2="22" y2="27" stroke="#2d6b95" stroke-width="2"/>
    <circle cx="12" cy="31" r="1.6" fill="#2d6b95"/>
  </svg>
  <p class="abs phone-number">719-555-0148</p>
  <p class="abs email">rcharlow@example.com</p>
  <div class="abs footer-rule second"></div>
  <span class="abs social" style="left:414px" aria-label="Social profile"></span>
  <span class="abs social" style="left:454px" aria-label="Social profile"></span>
  <span class="abs social" style="left:495px" aria-label="Social profile"></span>
  <span class="abs social" style="left:533px" aria-label="Social profile"></span>

</main>
</body>
</html>
```